New business card design for Pinecrest Hollow Optometry Clinic

We need a new business card design using our existing logo (uploaded). Please do not include eyes, eye exam charts or beaches, water, sand. The logo I uploaded shows our colors of green and blue, but we are open to seeing it in black OR white. We would like to see something modern and fresh. It will need to be 2 sided. On the front we will need to be able to put a doctors name, for example-Dr Marta Kellerman and Associates. We will need to be able to change the name to other doctors names when we send for printing. The back of the card should list the following: 3817 Tarrow St, Wasaga Beach (P)705-555-0148 (E) info@phoc.ca www.phoc.ca. "We are welcoming new patients" and a line for the appointment date and time. I have uploaded the back of a card to give an example

```html
<!DOCTYPE html>
<html lang="en">
<head>
<meta charset="utf-8">
<title>Pinecrest Hollow Optometry Clinic — Business Card</title>
<link rel="stylesheet" href="https://fonts.googleapis.com/css2?family=Montserrat:wght@500;700;800&display=swap">
<style>
  :root {
    --clinic-blue: #3a4fa3;
    --clinic-green: #1f9d4c;
    --card-white: #f4f4f3;
    --ink: #2a2a2a;
    --backdrop: #d9dadc;
    --rule: #333333;
  }
  * { box-sizing: border-box; margin: 0; padding: 0; }
  html, body {
    width: 1200px; height: 801px; overflow: hidden;
    background: var(--backdrop);
    font-family: "Montserrat", Arial, sans-serif;
  }
  .canvas { position: relative; width: 1200px; height: 801px; }

  .card {
    position: absolute;
    width: 540px; height: 309px;
    border-radius: 14px;
    background: linear-gradient(135deg, #f7f7f6 0%, #ececeb 100%);
    box-shadow: 0 10px 24px rgba(0,0,0,.22);
    overflow: hidden;
  }
  .card-front { left: 40px; top: 120px; }
  .card-back { left: 620px; top: 372px; }

  .card-surface {
    position: absolute; inset: 0;
    background: linear-gradient(160deg, #f6f6f5, #e8e8e6);
  }

  /* Front */
  .front-body {
    position: absolute; inset: 0;
    display: flex; flex-direction: column; align-items: center; justify-content: center;
    gap: 26px;
  }
  .brand { display: flex; align-items: center; gap: 12px; }
  .brand-dot { width: 26px; height: 26px; border-radius: 50%; background: var(--clinic-green); flex: none; }
  .brand-name {
    font-weight: 800; color: var(--clinic-blue);
    font-size: 25px; line-height: 1.15; letter-spacing: .2px;
  }
  .doctor-name {
    font-weight: 800; color: var(--clinic-blue);
    font-size: 24px; letter-spacing: .3px;
  }

  /* Back */
  .back-band {
    position: absolute; left: 0; top: 0; width: 100%; height: 128px;
    background: linear-gradient(90deg, var(--clinic-blue) 0%, #2e7d8c 55%, var(--clinic-green) 100%);
    display: flex; align-items: center; justify-content: center;
  }
  .back-band .brand-name { color: #ffffff; font-size: 19px; }
  .back-band .brand-dot { background: #ffffff; width: 20px; height: 20px; }

  .back-content { position: absolute; left: 0; top: 134px; width: 100%; text-align: center; }
  .welcome {
    font-weight: 800; color: var(--clinic-blue);
    font-size: 24px; letter-spacing: .2px;
  }
  .contact-line {
    margin-top: 8px;
    display: flex; justify-content: center; align-items: center; gap: 8px;
    font-weight: 500; color: var(--ink); font-size: 13px;
  }
  .contact-item { display: inline-flex; align-items: center; gap: 4px; }
  .contact-item svg { width: 11px; height: 11px; fill: var(--clinic-green); }
  .address { margin-top: 5px; font-weight: 500; color: var(--ink); font-size: 13px; }

  .booking { position: absolute; left: 34px; right: 30px; bottom: 22px; }
  .booking-row { display: flex; align-items: flex-end; gap: 8px; margin-top: 14px; }
  .booking-label { font-weight: 700; color: var(--clinic-green); font-size: 13px; white-space: nowrap; }
  .booking-line { flex: 1; border-bottom: 1px solid var(--rule); height: 1px; margin-bottom: 3px; }
</style>
</head>
<body>
<main class="canvas">

  <section class="card card-front" aria-label="Card front">
    <div class="card-surface"></div>
    <div class="front-body">
      <div class="brand">
        <span class="brand-dot"></span>
        <span class="brand-name">Pinecrest Hollow<br>Optometry Clinic</span>
      </div>
      <p class="doctor-name">Dr Marta Kellerman and Associates</p>
    </div>
  </section>

  <section class="card card-back" aria-label="Card back">
    <div class="card-surface"></div>
    <header class="back-band">
      <div class="brand">
        <span class="brand-dot"></span>
        <span class="brand-name">Pinecrest Hollow<br>Optometry Clinic</span>
      </div>
    </header>

    <div class="back-content">
      <h1 class="welcome">We are welcoming new patients!</h1>
      <p class="contact-line">
        <span class="contact-item">
          <svg viewBox="0 0 24 24" aria-hidden="true"><path d="M6.6 10.8a15.1 15.1 0 0 0 6.6 6.6l2.2-2.2a1 1 0 0 1 1-.25 11.4 11.4 0 0 0 3.6.57 1 1 0 0 1 1 1V20a1 1 0 0 1-1 1A17 17 0 0 1 3 4a1 1 0 0 1 1-1h3.5a1 1 0 0 1 1 1c0 1.25.2 2.45.57 3.57a1 1 0 0 1-.25 1z"/></svg>
          705-555-0148
        </span>
        <span class="contact-item">
          <svg viewBox="0 0 24 24" aria-hidden="true"><path d="M2 5h20v14H2z M4 7v.5l8 5 8-5V7l-8 5z" fill-rule="evenodd"/></svg>
          info@phoc.ca
        </span>
        <span class="contact-item">
          <svg viewBox="0 0 24 24" aria-hidden="true"><circle cx="12" cy="12" r="10"/></svg>
          www.phoc.ca
        </span>
      </p>
      <p class="address">3817 Tarrow St, Wasaga Beach</p>
    </div>

    <div class="booking">
      <div class="booking-row">
        <span class="booking-label">Appointment:</span>
        <span class="booking-line"></span>
      </div>
      <div class="booking-row">
        <span class="booking-label">Date:</span>
        <span class="booking-line"></span>
        <span class="booking-label">Time:</span>
        <span class="booking-line"></span>
      </div>
    </div>
  </section>

</main>
</body>
</html>
```